Verostel business card

Business card for sustainable investment company called "Verostel". Verostel is an exchange platform selling carbon credits between buyers and sellers. Carbon Credits are an environmental commodity for reducing global carbon emissions.

the card should obviously have our logo and the theme should be sustainability/environment mixed with a trading platform.

Contact Information for Business Card

Logo, Name, Title, Phone, Email

Colors
0054AA
0677BA
7BADD7
CADEEF
E8F1F8
0094D4
00A9DD
6FCCEA
C7EBF8
E9F6FB
00AB8E
00BBA5
67D7C9
C6EFE9
E9F9F6
59FF00
82FF00
B8FF75
E3FFCB
F4FFEA

```html
<!DOCTYPE html>
<html lang="en">
<head>
<meta charset="utf-8">
<title>Verostel business card</title>
<link rel="stylesheet" href="https://fonts.googleapis.com/css2?family=Poppins:wght@400;500;600;700&display=swap">
<style>
  :root {
    --backdrop: #d9dadc;
    --card-white: #f4fffa;
    --navy: #0f3346;
    --navy-deep: #0a2f45;
    --navy-mid: #0d4a5e;
    --ocean-blue: #0677ba;
    --teal: #00ab8e;
    --teal-light: #00bba5;
    --mint: #67d7c9;
    --leaf-green: #82ff00;
    --swoosh-pale: #c6efe9;
    --text-dark: #0f3346;
    --text-light: #ffffff;
  }
  * { box-sizing: border-box; margin: 0; padding: 0; }
  html, body { width: 1200px; height: 799px; overflow: hidden; }
  body {
    background: var(--backdrop);
    font-family: "Poppins", sans-serif;
    position: relative;
  }
  .card {
    position: absolute;
    top: 245px;
    width: 540px;
    height: 310px;
    border-radius: 22px;
    overflow: hidden;
    box-shadow: 0 14px 30px rgba(0,0,0,0.18);
  }
  .card-front { left: 45px; background: var(--card-white); }
  .card-back {
    left: 615px;
    background: linear-gradient(135deg, var(--navy-mid), var(--navy-deep));
    border-bottom: 3px solid var(--teal-light);
  }
  .front-waves { position: absolute; inset: 0; width: 540px; height: 310px; }
  .brand-block { position: absolute; left: 34px; top: 96px; }
  .brand-name {
    display: flex; align-items: center; gap: 10px;
    font-weight: 600; font-size: 30px; letter-spacing: 1px;
    color: var(--text-dark);
  }
  .brand-mark {
    width: 22px; height: 22px; background: var(--teal);
  }
  .person { position: absolute; left: 34px; top: 182px; }
  .person-name {
    font-weight: 600; font-size: 20px; letter-spacing: 0.5px;
    color: var(--teal);
  }
  .person-title { font-size: 13px; color: var(--text-dark); margin-top: 2px; }
  .contact-list {
    position: absolute; right: 22px; top: 58px;
    list-style: none; text-align: right;
    color: var(--text-light); font-size: 12.5px; line-height: 1.5;
  }
  .contact-list li { display: flex; justify-content: flex-end; align-items: center; gap: 9px; }
  .contact-list .gap { margin-bottom: 8px; }
  .contact-list svg { width: 12px; height: 12px; flex: none; }
  .contact-list .blank { width: 12px; flex: none; }
  .back-brand {
    position: absolute; inset: 0;
    display: flex; align-items: center; justify-content: center; gap: 16px;
    font-weight: 600; font-size: 48px; letter-spacing: 2px;
    color: var(--mint);
  }
  .back-brand .brand-mark { width: 40px; height: 40px; background: var(--leaf-green); }
</style>
</head>
<body>
  <section class="card card-front">
    <svg class="front-waves" viewBox="0 0 540 310" aria-hidden="true">
      <path d="M392,0 C300,70 330,215 150,310 L540,310 L540,0 Z" fill="var(--navy)"/>
      <path d="M370,0 C282,70 306,210 122,310" fill="none" stroke="var(--swoosh-pale)" stroke-width="14"/>
      <path d="M356,0 C268,72 292,205 100,310" fill="none" stroke="var(--teal)" stroke-width="9"/>
      <path d="M346,0 C262,80 286,200 86,310" fill="none" stroke="var(--leaf-green)" stroke-width="3"/>
      <path d="M0,258 C70,290 130,300 190,310 L0,310 Z" fill="var(--ocean-blue)"/>
      <path d="M0,270 C70,298 130,305 170,310 L0,310 Z" fill="var(--card-white)"/>
      <path d="M210,310 C260,290 300,270 330,240" fill="none" stroke="var(--mint)" stroke-width="3"/>
    </svg>

    <div class="brand-block">
      <div class="brand-name"><span class="brand-mark"></span>VEROSTEL</div>
    </div>

    <div class="person">
      <p class="person-name">DANIEL HARPER</p>
      <p class="person-title">Managing Director</p>
    </div>

    <ul class="contact-list">
      <li>4120 Cedar Hollow Road<span class="blank"></span></li>
      <li class="gap">Juneau, Alaska 34512<span class="blank"></span></li>
      <li>555-201-4478
        <svg viewBox="0 0 24 24"><path fill="#fff" d="M6.6 10.8a15 15 0 0 0 6.6 6.6l2.2-2.2c.3-.3.7-.4 1-.2 1.1.4 2.3.6 3.6.6.6 0 1 .4 1 1V20c0 .6-.4 1-1 1A17 17 0 0 1 3 4c0-.6.4-1 1-1h3.5c.6 0 1 .4 1 1 0 1.3.2 2.5.6 3.6.1.3 0 .7-.2 1z"/></svg>
      </li>
      <li class="gap">555-309-6612
        <svg viewBox="0 0 24 24"><rect x="6" y="2" width="12" height="20" rx="2" fill="none" stroke="#fff" stroke-width="2"/></svg>
      </li>
      <li>info@verostel.com
        <svg viewBox="0 0 24 24"><rect x="2" y="5" width="20" height="14" rx="1" fill="#fff"/><path d="M2 6l10 7 10-7" fill="none" stroke="var(--navy)" stroke-width="2"/></svg>
      </li>
      <li>www.verostel.com
        <svg viewBox="0 0 24 24"><circle cx="12" cy="12" r="10" fill="none" stroke="#fff" stroke-width="2"/><path d="M2 12h20M12 2c3 3 3 17 0 20M12 2c-3 3-3 17 0 20" fill="none" stroke="#fff" stroke-width="1.5"/></svg>
      </li>
    </ul>
  </section>

  <section class="card card-back">
    <div class="back-brand"><span class="brand-mark"></span>VEROSTEL</div>
  </section>
</body>
</html>
```